Simple design for eCommerce retailer of Custom Cut Mirror Frames

We need a fresh design for our eCommerce store. Currently, we need a design for each page on the existing site.

Here is the site as it stands right now: glassvela.com

Here is a competitor site that we like. The owner really likes the block look for the home page: framorly.com

Here is a video we would like to feature: https://videohost.example/v/Kp7rTq2LmXa

Here is the color palate, emphasis on the green and purple: https://palettes.example/quiet-bay-theme-48271953/?showPublished=true

Here is an example of a landing page we are currently using: https://glassvela.com/lander-10-off-install/

Font for the site should be the google font Lato

Home page should include the following sections/blocks:

How it works
Shop now
Testimonials
Featured Products
Before and After Gallery
Updates

My team has been slow getting back to me with feedback. I'm pushing them to speed their process up.

Target Market(s)

Women, Ages 35-65+

Number of Pages Required

5+ page

Font styles to use
Sans Serif

Requirements
Must have
• -Before and after gallery
• -Star ratings
• -eCommerce look and feel
• -Info about being able to order free samples
• -Language from the checkmarks on the landing page
• -sleek product page
• -home page should be have a very modern design feel
Should not have
• Product Prices...the user has to use the calculator to determine the price of their purchase.
• Sliders

```html
<!DOCTYPE html>
<html lang="en">
<head>
<meta charset="utf-8">
<title>Glassvela — Frame Any Mirror In Your House</title>
<link href="https://fonts.googleapis.com/css2?family=Lato:wght@300;400;700;900&display=swap" rel="stylesheet">
<style>
:root{
  --teal:#6fa8a3;
  --teal-dark:#4f8782;
  --purple:#9c6b92;
  --purple-dark:#7f5277;
  --ink:#3d4447;
  --text:#6b7174;
  --muted:#9aa0a3;
  --line:#e4e7e8;
  --soft:#f3f4f5;
  --white:#ffffff;
  --dark:#2d3235;
  --star:#e8b74a;
}
*{box-sizing:border-box;margin:0;padding:0}
html,body{width:1200px;height:4264px;overflow:hidden}
body{font-family:"Lato",Arial,sans-serif;color:var(--text);background:var(--white);font-size:13px;line-height:1.6}
a{color:inherit;text-decoration:none}
.wrap{width:1080px;margin:0 auto;position:relative}
.btn{display:inline-block;background:var(--purple);color:var(--white);font-size:10px;font-weight:700;letter-spacing:1.2px;text-transform:uppercase;padding:8px 22px;border-radius:2px}
.section-title{font-size:30px;font-weight:700;color:var(--ink);text-align:center}
.stars{color:var(--star);font-size:13px;letter-spacing:2px}

.topbar{height:48px;border-bottom:1px solid var(--line);font-size:11px;color:var(--text)}
.topbar .wrap{display:flex;align-items:center;height:48px;gap:34px}
.topbar .account{margin-left:auto}
.topbar svg{vertical-align:-2px;margin-right:6px}

.header{height:80px}
.header .wrap{display:flex;align-items:center;height:80px}
.brand{display:flex;align-items:center;gap:10px;font-size:24px;font-weight:700;color:var(--purple)}
.brand-mark{width:22px;height:22px;background:var(--teal)}
.nav{margin-left:auto;display:flex;gap:40px;font-size:11px;font-weight:700;letter-spacing:1px;color:var(--ink);text-transform:uppercase}

.hero{height:520px;position:relative;overflow:hidden}
.hero-photo{position:absolute;inset:0;background:linear-gradient(120deg,#9fbcb9 0%,#8fb0ad 40%,#b6a9b4 100%)}
.hero-overlay{position:absolute;inset:0;background:rgba(95,150,145,.45)}
.hero-copy{position:relative;text-align:center;padding-top:100px;color:var(--white)}
.hero-copy h1{font-size:54px;font-weight:900;line-height:1.08;letter-spacing:1px}
.hero-copy p{font-size:16px;margin:10px 0 26px;opacity:.9}
.hero-arrow{position:absolute;top:230px;color:var(--white);font-size:22px;opacity:.8}
.hero-arrow.left{left:20px}.hero-arrow.right{right:20px}
.hero-wave{position:absolute;left:0;bottom:0;width:1200px;height:110px}

.how{height:392px;padding-top:40px}
.how-grid{display:grid;grid-template-columns:repeat(4,1fr);gap:40px;margin-top:34px;text-align:center}
.how-item svg{margin-bottom:12px}
.how-item h3{font-size:14px;font-weight:700;color:var(--ink);line-height:1.35;height:40px}
.how-item p{font-size:11px;line-height:1.6;margin:8px 0 16px;height:52px}

.feature{height:300px;display:flex;align-items:center}
.feature-inner{display:flex;width:1200px;height:240px}
.video-panel{width:560px;background:var(--teal);padding:30px 0 0 120px}
.video-thumb{width:260px;height:140px;background:linear-gradient(135deg,#c9c4c6,#8e9a9b);position:relative;border:4px solid var(--white)}
.video-play{position:absolute;left:50%;top:50%;transform:translate(-50%,-50%)}
.video-panel .btn{margin-top:14px;background:var(--purple-dark)}
.checks{flex:1;display:grid;grid-template-columns:1fr 1fr;gap:14px 30px;padding:36px 40px 0 56px;align-content:start}
.checks li{list-style:none;font-size:12px;display:flex;align-items:center;gap:10px}

.guarantee{height:260px;position:relative;text-align:center;color:var(--white)}
.guarantee-photo{position:absolute;inset:0;background:linear-gradient(90deg,#b48fb0,#a3779c 50%,#b89ab4)}
.guarantee-copy{position:relative;padding-top:72px}
.guarantee h2{font-size:34px;font-weight:900}
.guarantee p{font-size:20px;margin:6px 0 18px}
.guarantee .btn{background:var(--teal)}

.products{height:512px;padding-top:44px}
.product-row{display:flex;justify-content:space-between;margin-top:40px;padding:0 20px}
.product{width:170px;text-align:center;padding:14px 0 16px}
.product.active{box-shadow:0 4px 18px rgba(0,0,0,.12)}
.product-img{width:130px;height:170px;margin:0 auto 12px;position:relative}
.product-img .btn{position:absolute;left:50%;bottom:12px;transform:translateX(-50%);padding:5px 12px;font-size:9px}
.product h4{font-size:12px;font-weight:700;color:var(--ink)}
.product small{display:block;font-size:11px;color:var(--muted);margin-bottom:4px}

.values{height:288px;display:flex}
.value{flex:1;position:relative;color:var(--white);text-align:center;padding:40px 40px 0}
.value h3{font-size:22px;font-weight:900;line-height:1.1;text-transform:uppercase}
.value h5{font-size:10px;letter-spacing:1px;opacity:.85;margin:4px 0 14px;text-transform:uppercase}
.value p{font-size:11px;line-height:1.6;opacity:.9;margin-bottom:18px}
.value > *{position:relative}
.value-photo{position:absolute!important;inset:0}

.testimonials{height:340px;background:var(--soft);padding-top:40px;text-align:center}
.avatar{width:56px;height:56px;border-radius:50%;background:#bfc3c5;margin:34px auto 10px}
.testimonials .who{font-size:12px;font-weight:700;color:var(--ink)}
.testimonials .role{font-size:10px;color:var(--muted)}
.testimonials blockquote{width:820px;margin:16px auto 0;font-size:12px;line-height:1.8}
.t-arrow{position:absolute;top:110px;width:36px;height:36px;border-radius:50%;background:var(--purple);color:var(--white);font-size:18px;line-height:34px;text-align:center}
.t-arrow.left{left:40px}.t-arrow.right{right:40px}

.gallery{height:600px;padding-top:44px}
.gallery-grid{display:grid;grid-template-columns:1.1fr 1fr 1fr 1.1fr 1fr 1fr 1.1fr;grid-template-rows:208px 208px;gap:4px;margin-top:34px}
.gallery-grid div{position:relative}
.gallery-grid .wide{grid-column:span 2}
.gallery-grid .cap{position:absolute;left:10px;bottom:10px;color:var(--white);font-size:12px;font-weight:700}
.dots{display:flex;justify-content:center;gap:8px;margin-top:16px}
.dots span{width:8px;height:8px;border-radius:50%;background:#cfd3d4}
.dots span.on{background:var(--teal)}

.articles{height:468px;padding-top:30px}
.article-row{display:flex;justify-content:center;gap:28px;margin-top:36px}
.article{width:300px}
.article-img{height:150px;margin-bottom:14px}
.article h4{font-size:13px;font-weight:700;color:var(--ink);line-height:1.35}
.article p{font-size:11px;margin:6px 0 10px}
.article a{font-size:10px;font-weight:700;color:var(--teal);letter-spacing:1px;text-transform:uppercase}

.newsletter{height:80px;background:var(--teal);color:var(--white)}
.newsletter .wrap{display:flex;align-items:center;height:80px;gap:16px}
.newsletter h4{font-size:18px;font-weight:700;line-height:1.2}
.newsletter p{font-size:11px;opacity:.9}
.news-form{margin-left:auto;display:flex}
.news-form span{width:200px;height:30px;background:var(--white);color:var(--muted);font-size:11px;padding:7px 12px}
.news-form .btn{border-radius:0;background:var(--purple);padding:8px 18px}

.footer{height:340px;padding-top:36px}
.footer .wrap{display:grid;grid-template-columns:1.4fr 1fr 1fr 1.2fr;gap:40px}
.footer h5{font-size:14px;font-weight:700;color:var(--ink);margin-bottom:12px}
.footer li{list-style:none;font-size:11px;line-height:2}
.footer .about p{font-size:11px;margin-top:14px}
.pay{display:flex;gap:6px;margin-top:8px}
.pay span{width:34px;height:22px;border-radius:3px;background:#c7cbcd}
.bottom{height:36px;border-top:1px solid var(--line);text-align:center;font-size:10px;color:var(--muted);line-height:36px}
</style>
</head>
<body>

<div class="topbar">
  <div class="wrap">
    <span><svg width="11" height="11" viewBox="0 0 24 24"><path d="M6.6 10.8a15 15 0 0 0 6.6 6.6l2.2-2.2c.3-.3.7-.4 1-.2 1.1.4 2.3.6 3.6.6.6 0 1 .4 1 1V20c0 .6-.4 1-1 1A17 17 0 0 1 3 4c0-.6.4-1 1-1h3.5c.6 0 1 .4 1 1 0 1.3.2 2.5.6 3.6.1.3 0 .7-.2 1z" fill="#6fa8a3"/></svg>Call Us Today: (555) 014-2387</span>
    <span><svg width="10" height="12" viewBox="0 0 20 24"><path d="M10 0a8 8 0 0 0-8 8c0 6 8 16 8 16s8-10 8-16a8 8 0 0 0-8-8zm0 11a3 3 0 1 1 0-6 3 3 0 0 1 0 6z" fill="#6fa8a3"/></svg>2450 Harbor Row, Lakeside, CA 90000</span>
    <span class="account">Login or Register</span>
  </div>
</div>

<header class="header">
  <div class="wrap">
    <a class="brand" href="#"><span class="brand-mark"></span>Glassvela</a>
    <nav class="nav">
      <a href="#">Shop Framing Kits</a>
      <a href="#">Custom Framed Mirrors</a>
      <a href="#">View Styles</a>
      <a href="#">Before &amp; After Gallery</a>
    </nav>
  </div>
</header>

<section class="hero">
  <div class="hero-photo" role="img" aria-label="Bathroom vanity with a large framed mirror"></div>
  <div class="hero-overlay"></div>
  <span class="hero-arrow left">&#8249;</span><span class="hero-arrow right">&#8250;</span>
  <div class="hero-copy">
    <h1>FRAME ANY MIRROR<br>IN YOUR HOUSE</h1>
    <p>Custom cut frames, made to fit your mirror</p>
    <a class="btn" href="#">Shop Framing Kits</a>
  </div>
  <svg class="hero-wave" viewBox="0 0 1200 110" preserveAspectRatio="none">
    <polygon points="0,40 700,100 0,110" fill="#6fa8a3"/>
    <polygon points="1200,20 500,110 1200,110" fill="#9c6b92"/>
    <polygon points="0,80 600,60 1200,90 1200,110 0,110" fill="#ffffff"/>
  </svg>
</section>

<section class="how">
  <div class="wrap">
    <h2 class="section-title">How it Works</h2>
    <div class="how-grid">
      <div class="how-item">
        <svg width="34" height="34" viewBox="0 0 34 34"><rect x="3" y="3" width="28" height="28" fill="none" stroke="#6fa8a3" stroke-width="2"/><rect x="9" y="9" width="16" height="16" fill="none" stroke="#6fa8a3" stroke-width="1.5"/></svg>
        <h3>Frames Delivered Ready<br>To Install</h3>
        <p>Each frame is cut to your exact size and ships with all you need to finish the job.</p>
        <a class="btn" href="#">Details</a>
      </div>
      <div class="how-item">
        <svg width="34" height="34" viewBox="0 0 34 34"><path d="M5 29 L29 5 M22 5h7v7" fill="none" stroke="#6fa8a3" stroke-width="2"/><rect x="3" y="3" width="28" height="28" fill="none" stroke="#6fa8a3" stroke-width="1.5"/></svg>
        <h3>How to Measure<br>Your Mirror Frame</h3>
        <p>Take two quick readings of width and height and our calculator does the rest.</p>
        <a class="btn" href="#">Details</a>
      </div>
      <div class="how-item">
        <svg width="34" height="34" viewBox="0 0 34 34"><rect x="5" y="8" width="24" height="20" fill="none" stroke="#6fa8a3" stroke-width="2"/><path d="M11 8V5h12v3" fill="none" stroke="#6fa8a3" stroke-width="2"/></svg>
        <h3>Why Frame Your<br>Bathroom Mirror</h3>
        <p>A simple frame turns a plain glass sheet into a finished, custom piece of decor.</p>
        <a class="btn" href="#">Details</a>
      </div>
      <div class="how-item">
        <svg width="34" height="34" viewBox="0 0 34 34"><rect x="3" y="6" width="28" height="22" fill="none" stroke="#6fa8a3" stroke-width="2"/><path d="M3 6l10 10M31 6L21 16" stroke="#6fa8a3" stroke-width="1.5"/></svg>
        <h3>Large Or<br>Unique Mirrors</h3>
        <p>Oversized or odd shaped glass? Send us your sizes and we will find a fit.</p>
        <a class="btn" href="#">Details</a>
      </div>
    </div>
  </div>
</section>

<section class="feature">
  <div class="feature-inner">
    <div class="video-panel">
      <div class="video-thumb" role="img" aria-label="Video still of a mirror frame being installed">
        <svg class="video-play" width="46" height="32" viewBox="0 0 46 32"><rect width="46" height="32" rx="7" fill="#3d4447" opacity=".85"/><polygon points="18,9 30,16 18,23" fill="#fff"/></svg>
      </div>
      <a class="btn" href="#">Watch the Video</a>
    </div>
    <ul class="checks">
      <li><svg width="16" height="16" viewBox="0 0 16 16"><circle cx="8" cy="8" r="7" fill="none" stroke="#9c6b92" stroke-width="1.3"/><path d="M4.5 8.2l2.3 2.2 4.7-4.8" fill="none" stroke="#9c6b92" stroke-width="1.5"/></svg>DIY in 15 minutes</li>
      <li><svg width="16" height="16" viewBox="0 0 16 16"><circle cx="8" cy="8" r="7" fill="none" stroke="#9c6b92" stroke-width="1.3"/><path d="M4.5 8.2l2.3 2.2 4.7-4.8" fill="none" stroke="#9c6b92" stroke-width="1.5"/></svg>Free samples to try at home</li>
      <li><svg width="16" height="16" viewBox="0 0 16 16"><circle cx="8" cy="8" r="7" fill="none" stroke="#9c6b92" stroke-width="1.3"/><path d="M4.5 8.2l2.3 2.2 4.7-4.8" fill="none" stroke="#9c6b92" stroke-width="1.5"/></svg>Install with mirror clips on</li>
      <li><svg width="16" height="16" viewBox="0 0 16 16"><circle cx="8" cy="8" r="7" fill="none" stroke="#9c6b92" stroke-width="1.3"/><path d="M4.5 8.2l2.3 2.2 4.7-4.8" fill="none" stroke="#9c6b92" stroke-width="1.5"/></svg>Protects mirror edges from rust</li>
      <li><svg width="16" height="16" viewBox="0 0 16 16"><circle cx="8" cy="8" r="7" fill="none" stroke="#9c6b92" stroke-width="1.3"/><path d="M4.5 8.2l2.3 2.2 4.7-4.8" fill="none" stroke="#9c6b92" stroke-width="1.5"/></svg>Over 60 styles and finishes</li>
      <li><svg width="16" height="16" viewBox="0 0 16 16"><circle cx="8" cy="8" r="7" fill="none" stroke="#9c6b92" stroke-width="1.3"/><path d="M4.5 8.2l2.3 2.2 4.7-4.8" fill="none" stroke="#9c6b92" stroke-width="1.5"/></svg>Color matched corner blocks</li>
      <li><svg width="16" height="16" viewBox="0 0 16 16"><circle cx="8" cy="8" r="7" fill="none" stroke="#9c6b92" stroke-width="1.3"/><path d="M4.5 8.2l2.3 2.2 4.7-4.8" fill="none" stroke="#9c6b92" stroke-width="1.5"/></svg>Affordable vs. a new mirror</li>
      <li><svg width="16" height="16" viewBox="0 0 16 16"><circle cx="8" cy="8" r="7" fill="none" stroke="#9c6b92" stroke-width="1.3"/><path d="M4.5 8.2l2.3 2.2 4.7-4.8" fill="none" stroke="#9c6b92" stroke-width="1.5"/></svg>100% satisfaction guarantee</li>
      <li><svg width="16" height="16" viewBox="0 0 16 16"><circle cx="8" cy="8" r="7" fill="none" stroke="#9c6b92" stroke-width="1.3"/><path d="M4.5 8.2l2.3 2.2 4.7-4.8" fill="none" stroke="#9c6b92" stroke-width="1.5"/></svg>Fifth generation craftsmen</li>
      <li><svg width="16" height="16" viewBox="0 0 16 16"><circle cx="8" cy="8" r="7" fill="none" stroke="#9c6b92" stroke-width="1.3"/><path d="M4.5 8.2l2.3 2.2 4.7-4.8" fill="none" stroke="#9c6b92" stroke-width="1.5"/></svg>Outstanding customer support</li>
    </ul>
  </div>
</section>

<section class="guarantee">
  <div class="guarantee-photo" role="img" aria-label="Bright bathroom with a framed vanity mirror"></div>
  <div class="guarantee-copy">
    <h2>100% SATISFACTION GUARANTEE!</h2>
    <p>Unsure? - Don't Worry, We Will Walk You Through Every Step Of The Process.</p>
    <a class="btn" href="#">Learn More</a>
  </div>
</section>

<section class="products">
  <div class="wrap">
    <h2 class="section-title">Featured Products</h2>
    <div class="product-row">
      <div class="product active">
        <div class="product-img" role="img" aria-label="Dark walnut mirror frame sample" style="background:linear-gradient(135deg,#4a3a30,#2c2420)"><a class="btn" href="#">View</a></div>
        <h4>Linden Mocha Ripple</h4><small>Mirror Frame Kit</small><div class="stars">★★★★★</div>
      </div>
      <div class="product">
        <div class="product-img" role="img" aria-label="Rich cherry mirror frame sample" style="background:linear-gradient(135deg,#7a3f2a,#4e2819)"></div>
        <h4>Aster Cherry Grain</h4><small>Mirror Frame Kit</small><div class="stars">★★★★★</div>
      </div>
      <div class="product">
        <div class="product-img" role="img" aria-label="Espresso mirror frame sample" style="background:linear-gradient(135deg,#3a3330,#1e1a18)"></div>
        <h4>Aster Espresso Tone</h4><small>Mirror Frame Kit</small><div class="stars">★★★★★</div>
      </div>
      <div class="product">
        <div class="product-img" role="img" aria-label="Antique bronze mirror frame sample" style="background:linear-gradient(135deg,#5c4a38,#2f2620)"></div>
        <h4>Marlow Espresso</h4><small>Mirror Frame Kit</small><div class="stars">★★★★★</div>
      </div>
      <div class="product">
        <div class="product-img" role="img" aria-label="Brushed gold mirror frame sample" style="background:linear-gradient(135deg,#a27c4a,#6b5030)"></div>
        <h4>Marlow Gold Leaf</h4><small>Mirror Frame Kit</small><div class="stars">★★★★★</div>
      </div>
    </div>
  </div>
</section>

<section class="values">
  <div class="value">
    <div class="value-photo" role="img" aria-label="Framed mirror over a bathroom vanity, darkened" style="background:linear-gradient(135deg,#5b5f61,#2d3235)"></div>
    <h3>Satisfaction<br>Guaranteed</h3><h5>Guaranteed To Fit</h5>
    <p>If your frame does not fit or you are not happy with it, we will make it right. Every kit is checked before it leaves our shop so you can order with confidence.</p>
    <a class="btn" href="#">Learn More</a>
  </div>
  <div class="value">
    <div class="value-photo" role="img" aria-label="Hands fitting a mirror frame, darkened" style="background:linear-gradient(135deg,#6a6c6b,#3a3e40)"></div>
    <h3>Quick &amp; Easy<br>Installation</h3><h5>Install In Minutes</h5>
    <p>No tools needed beyond what ships in the box. Peel, press and enjoy a finished mirror in about fifteen minutes, clips and all.</p>
    <a class="btn" href="#">Learn More</a>
  </div>
  <div class="value">
    <div class="value-photo" role="img" aria-label="Large framed wall mirror, darkened" style="background:linear-gradient(135deg,#55595b,#2a2e30)"></div>
    <h3>Large Or<br>Unique Frames?</h3><h5>&nbsp;</h5>
    <p>We frame big, wide and oddly shaped mirrors too. Send us your sizes and our team will help you plan the right frame.</p>
    <a class="btn" href="#">Learn More</a>
  </div>
</section>

<section class="testimonials">
  <div class="wrap">
    <h2 class="section-title">Client Testimonials</h2>
    <span class="t-arrow left">&#8249;</span><span class="t-arrow right">&#8250;</span>
    <div class="avatar" role="img" aria-label="Customer portrait placeholder"></div>
    <div class="who">Barbara L.</div>
    <div class="role">Verified Buyer</div>
    <blockquote>"We needed to update the look of our bathroom and did not want to rip out the mirror. The frame came cut exactly to size, the samples helped us pick a finish, and it went up in one afternoon. It looks like a brand new custom piece and friends always ask where we got it."</blockquote>
  </div>
</section>

<section class="gallery">
  <h2 class="section-title">Featured Gallery</h2>
  <div class="gallery-grid">
    <div role="img" aria-label="Before and after of a framed bathroom mirror" style="background:linear-gradient(135deg,#a58766,#6d543c)"></div>
    <div role="img" aria-label="Vanity mirror with dark frame" style="background:linear-gradient(135deg,#c6b39a,#8a7359)"></div>
    <div role="img" aria-label="Framed mirror above double sink" style="background:linear-gradient(135deg,#8f8d86,#5a5650)"></div>
    <div role="img" aria-label="Bathroom with bronze framed mirror" style="background:linear-gradient(135deg,#b59a78,#7a6248)"></div>
    <div class="wide" role="img" aria-label="Wide vanity mirror with wood frame" style="background:linear-gradient(135deg,#cbb596,#94785a)"></div>
    <div role="img" aria-label="Framed mirror in a hallway" style="background:linear-gradient(135deg,#9e8a74,#64513f)"></div>
    <div role="img" aria-label="Before photo of an unframed mirror" style="background:linear-gradient(135deg,#c9b9a4,#8d7a64)"></div>
    <div role="img" aria-label="Installer fitting a frame on a mirror" style="background:linear-gradient(135deg,#9ba4a8,#5f686c)"></div>
    <div role="img" aria-label="Framed mirror over vanity lights" style="background:linear-gradient(135deg,#7f8a8c,#4a5254)"><span class="cap">Sorrel in Black</span></div>
    <div role="img" aria-label="Finished mirror with gold frame" style="background:linear-gradient(135deg,#b39873,#7a6447)"></div>
    <div role="img" aria-label="Long framed mirror in a master bath" style="background:linear-gradient(135deg,#a99a86,#6f604f)"></div>
    <div role="img" aria-label="Framed mirror with warm lighting" style="background:linear-gradient(135deg,#c0a582,#876c4e)"></div>
    <div role="img" aria-label="Framed mirror in a guest bath" style="background:linear-gradient(135deg,#b8a896,#7d6d5c)"></div>
  </div>
  <div class="dots"><span class="on"></span><span></span><span></span></div>
</section>

<section class="articles">
  <h2 class="section-title">Latest Articles</h2>
  <div class="article-row">
    <div class="article">
      <div class="article-img" role="img" aria-label="How to frame a bathroom mirror article image" style="background:linear-gradient(135deg,#8a7a6a,#4f443a)"></div>
      <h4>Framing Your Existing Bathroom Mirror</h4>
      <p>A step by step look at measuring, choosing a finish and fitting your new frame at home.</p>
      <a href="#">Read More</a>
    </div>
    <div class="article">
      <div class="article-img" role="img" aria-label="Product review article image" style="background:linear-gradient(135deg,#3a3f42,#1f2325)"></div>
      <h4>Product Review Spotlight: Framorly Kits &amp; Alternatives</h4>
      <p>We compare popular framing kits on fit, finish and how easy they are to put up.</p>
      <a href="#">Read More</a>
    </div>
    <div class="article">
      <div class="article-img" role="img" aria-label="Decor above a bathroom mirror article image" style="background:linear-gradient(135deg,#4a4e50,#2a2d2f)"></div>
      <h4>Decorating - What To Do Above Your Bathroom Mirrors</h4>
      <p>Fresh ideas for lights, shelves and art to finish the wall above your vanity mirror.</p>
      <a href="#">Read More</a>
    </div>
  </div>
</section>

<section class="newsletter">
  <div class="wrap">
    <svg width="34" height="26" viewBox="0 0 34 26"><rect x="1" y="1" width="32" height="24" fill="none" stroke="#fff" stroke-width="2"/><path d="M1 1l16 13L33 1" fill="none" stroke="#fff" stroke-width="2"/></svg>
    <div><h4>Sign Up to Newsletter</h4><p>Get tips, new styles and sample offers in your inbox.</p></div>
    <div class="news-form"><span>Your email address</span><a class="btn" href="#">Subscribe</a></div>
  </div>
</section>

<footer class="footer">
  <div class="wrap">
    <div class="about">
      <a class="brand" href="#"><span class="brand-mark"></span>Glassvela</a>
      <p>Custom cut mirror frames made to fit the mirror you already own. Order free samples and see every finish at home before you buy.</p>
    </div>
    <div>
      <h5>Company Info</h5>
      <ul><li>About Us</li><li>Privacy Policy</li><li>Terms &amp; Conditions</li><li>Shipping &amp; Returns</li><li>FAQ</li></ul>
    </div>
    <div>
      <h5>My Account</h5>
      <ul><li>My Account</li><li>Wishlist</li><li>Order History</li><li>Free Samples</li></ul>
    </div>
    <div>
      <h5>Contact Us</h5>
      <ul><li>2450 Harbor Row, Lakeside, CA 90000</li><li>hello@glassvela.com</li><li>(555) 014-2387</li></ul>
      <h5 style="margin-top:14px;margin-bottom:0">We Accept</h5>
      <div class="pay"><span></span><span></span><span></span><span></span></div>
    </div>
  </div>
</footer>
<div class="bottom">Copyright © 2024 Glassvela. All rights reserved.</div>

</body>
</html>
```